Lumenfield Holdings

Professional looking business card using darker colours
I do not yet have a logo for the company so feel free to suggest
The business is based on consultancy and project management
Based in Melbourne
Business card can omit the word "Holdings" and can be Lumenfield consulting etc.

Business

Contact Name on card : Tom Verisco Contact number : +61412 305 617 Email address will be confirmed shortly.

```html
<!DOCTYPE html>
<html lang="en">
<head>
<meta charset="utf-8">
<title>Lumenfield consulting – business card</title>
<link rel="stylesheet" href="https://fonts.googleapis.com/css2?family=Arimo:wght@400;500&display=swap">
<style>
  :root {
    --grey-light: #b4b4b4;
    --grey-dark: #2c2c2c;
    --navy-deep: #02021a;
    --navy-band: #0a0a52;
    --ring-grey: #4c4c58;
    --stripe-grey: #8c8c8c;
    --stripe-dark: #14141c;
    --ink: #000000;
    --paper: #ffffff;
  }
  html, body {
    margin: 0;
    padding: 0;
    width: 1200px;
    height: 686px;
    overflow: hidden;
    background: var(--paper);
  }
  .business-card {
    display: block;
    width: 1200px;
    height: 686px;
  }
  .card-text {
    font-family: "Arimo", Arial, sans-serif;
  }
  .company-name { font-size: 88px; font-weight: 400; }
  .email-label { font-size: 38px; font-weight: 500; fill: var(--ink); }
  .contact-line { font-size: 38px; font-weight: 500; fill: var(--paper); }
  .fill-ground-light { stop-color: var(--grey-light); }
  .fill-ground-dark { stop-color: var(--grey-dark); }
  .navy-disc { fill: var(--navy-deep); }
  .disc-ring { fill: var(--ring-grey); }
  .band-black { fill: var(--ink); }
  .band-navy { fill: var(--navy-band); }
  .stripe-grey { fill: var(--stripe-grey); }
  .stripe-dark { fill: var(--stripe-dark); }
</style>
</head>
<body>
<svg class="business-card" viewBox="0 0 1200 686" xmlns="http://www.w3.org/2000/svg" role="img" aria-label="Lumenfield consulting business card for Tom Verisco">
  <defs>
    <linearGradient id="ground-gradient" x1="0" y1="0" x2="1" y2="-0.15">
      <stop offset="0" class="fill-ground-light"/>
      <stop offset="0.75" class="fill-ground-dark"/>
    </linearGradient>
    <linearGradient id="name-gradient" gradientUnits="userSpaceOnUse" x1="130" y1="0" x2="1010" y2="0">
      <stop offset="0" stop-color="#0c0c0c"/>
      <stop offset="0.48" stop-color="#151515"/>
      <stop offset="0.64" stop-color="#f0f0f0"/>
      <stop offset="1" stop-color="#ffffff"/>
    </linearGradient>
    <clipPath id="disc-clip">
      <circle cx="1526" cy="480" r="816"/>
    </clipPath>
  </defs>

  <!-- ground -->
  <rect width="1200" height="686" fill="url(#ground-gradient)"/>
  <circle class="disc-ring" cx="1526" cy="480" r="838"/>
  <circle class="navy-disc" cx="1526" cy="480" r="816"/>

  <!-- company name -->
  <text class="card-text company-name" x="128" y="130" fill="url(#name-gradient)">Lumenfield consulting</text>

  <!-- bands -->
  <rect class="band-black" x="0" y="214" width="1200" height="186"/>
  <rect class="band-navy" x="0" y="403" width="1200" height="17"/>
  <rect class="band-black" x="0" y="420" width="1200" height="54"/>
  <rect class="stripe-grey" x="0" y="435" width="1200" height="6"/>
  <rect class="stripe-grey" x="0" y="460" width="1200" height="7"/>
  <g clip-path="url(#disc-clip)">
    <rect class="stripe-dark" x="0" y="435" width="1200" height="6"/>
    <rect class="stripe-dark" x="0" y="460" width="1200" height="7"/>
  </g>

  <!-- contact details -->
  <text class="card-text email-label" x="257" y="536">Email address:</text>
  <text class="card-text contact-line" x="1161" y="587" text-anchor="end">Contact Name on card : Tom Verisco</text>
  <text class="card-text contact-line" x="1161" y="639" text-anchor="end">Contact number : +61412 305 617</text>
</svg>
</body>
</html>
```